CD Cover Design Project

I need a cd cover design for my first 5-song EP which is going to be released on March 1st. I am a 19 year old female singer/songwriter based in Nashville, TN, and my style is somewhat singer/songwriter and/or pop/rock (ex: Vireya Talcombe, Doreen Pask...if you don't know these references, please check them out). I believe that simplicity is key, and this cover design should not be too overboard but should still express creativity with a touch of boldness, if that makes sense.
Updates
Can you all try putting the image with my hand in my hair (the mountains in the background) as the front cover and the bridge picture on the back cover?
I uploaded a picture of a font that i really like :) please check it out!
Hey everyone :) Thank you so much for submitting your awesome designs! We're all still swapping feedback and I'm still checking out what you all have created. I am uploading some examples of covers I really like, just so you can get the idea of what I like and dislike :) Thanks! Happy creating!
I AM UPLOADING A COLOR VERSION OF THE PICTURE I REALLY WANT TO USE AS THE FRONT COVER..... :)
Industry/Entity Type
Singer
Look and feel
Each slider illustrates characteristics of the customer's brand and the style your logo design should communicate.

```html
<!DOCTYPE html>
<html lang="en">
<head>
<meta charset="utf-8">
<title>EP Back Cover – Track List</title>
<link rel="stylesheet" href="https://fonts.googleapis.com/css2?family=Didact+Gothic&display=swap">
<style>
  :root {
    --sky: #c8cbd0;
    --treeline: #8a7a6c;
    --water-far: #5e6b7c;
    --water-mid: #4f5c6d;
    --dock-wood: #8e7159;
    --dock-shadow: #56575a;
    --water-near: #3d4850;
    --water-murk: #514b3a;
    --disc-fill: rgba(255, 255, 255, 0.55);
    --track-grey: #747474;
    --track-grey-dark: #5d5a57;
    --track-tan: #a87c5a;
    --track-tan-dark: #96704f;
  }
  html, body {
    margin: 0;
    padding: 0;
    overflow: hidden;
  }
  .cover {
    position: relative;
    width: 1200px;
    height: 919px;
    overflow: hidden;
    font-family: "Didact Gothic", "Century Gothic", sans-serif;
  }
  .cover__photo {
    position: absolute;
    inset: 0;
    background: linear-gradient(
      to bottom,
      var(--sky) 0%,
      var(--sky) 2%,
      var(--treeline) 6%,
      var(--treeline) 14%,
      var(--water-far) 17%,
      var(--water-mid) 40%,
      var(--dock-wood) 45%,
      var(--dock-wood) 60%,
      var(--dock-shadow) 66%,
      var(--water-near) 78%,
      var(--water-murk) 100%
    );
  }
  .cover__disc {
    position: absolute;
    left: 0;
    top: 0;
  }
  .tracklist {
    position: absolute;
    left: 0;
    top: 318px;
    width: 1200px;
    margin: 0;
    padding: 0;
    list-style: none;
    text-align: center;
    font-size: 41px;
    line-height: 61px;
    letter-spacing: 0.5px;
  }
  .tracklist li { margin: 0; padding-right: 0; }
  .track--1 { color: var(--track-grey); padding-left: 0; }
  .track--2 { color: var(--track-grey); }
  .track--3 { color: var(--track-tan); }
  .track--4 { color: var(--track-tan-dark); }
  .track--5 { color: var(--track-grey-dark); }
</style>
</head>
<body>
  <main class="cover">
    <div class="cover__photo" role="img" aria-label="Soft-focus photograph of a wooden boat dock on a lake, with a bare treeline on the far shore"></div>
    <svg class="cover__disc" width="1200" height="919" viewBox="0 0 1200 919" aria-hidden="true">
      <circle cx="617" cy="478" r="256" fill="var(--disc-fill)"/>
    </svg>
    <ol class="tracklist">
      <li class="track--1">1. rowdy</li>
      <li class="track--2">2. take a moment</li>
      <li class="track--3">3. sit back and wait</li>
      <li class="track--4">4. one more year</li>
      <li class="track--5">5. just for you</li>
    </ol>
  </main>
</body>
</html>
```